Riverstone & Pine Construction and Developments business cards

A business card with watermark background (construction work)

Company logo attached

Home improvement projects
House renovations
Bathroom and kitchen renovations
House extensions
New builds and granny flats

Director Omar Haddine
(Phone number)
omar@rpcbuildgroup.com.au
(Instagram logo) rpc_buildgroup

```html
<!DOCTYPE html>
<html lang="en">
<head>
<meta charset="utf-8">
<title>Riverstone &amp; Pine Construction and Developments – Business Cards</title>
<link href="https://fonts.googleapis.com/css2?family=Open+Sans:wght@400&family=Questrial&family=Roboto+Slab:wght@300&display=swap" rel="stylesheet">
<style>
  :root {
    --stage: #2e2e2e;
    --brand-blue: #2f78c4;
    --card-blue: #3f86cb;
    --rule-light: rgba(255,255,255,0.45);
    --rule-blue: #6f9fd6;
    --ink-grey: #555a60;
    --white: #ffffff;
  }
  * { box-sizing: border-box; margin: 0; padding: 0; }
  html, body { width: 1200px; height: 624px; overflow: hidden; background: var(--stage); }
  .canvas { position: relative; width: 1200px; height: 624px; }

  .card { position: absolute; top: 176px; width: 476px; height: 286px; overflow: hidden; }
  .card--services { left: 100px; background: var(--card-blue); }
  .card--contact { left: 624px; background: var(--white); }

  .card__photo { position: absolute; inset: 0; }
  .card--services .card__photo {
    background: radial-gradient(ellipse at 45% 55%, rgba(70,120,175,0.55), rgba(63,134,203,0) 65%),
                linear-gradient(160deg, #4a8dcf 0%, #3a7dc0 55%, #3f86cb 100%);
  }
  .card--contact .card__photo {
    background: radial-gradient(ellipse at 40% 40%, #e4e6e8 0%, #f1f2f3 45%, #fafafa 80%);
  }

  /* services side */
  .services { position: absolute; left: 45px; top: 102px; width: 386px; height: 82px;
    border-top: 1px solid var(--rule-light); border-bottom: 1px solid var(--rule-light);
    font-family: "Open Sans", sans-serif; font-size: 10.5px; color: var(--white); }
  .service { position: absolute; white-space: nowrap; display: flex; align-items: center; gap: 10px; }
  .service svg { width: 9px; height: 9px; }
  .service--newbuilds { left: 118px; top: 8px; }
  .service--home { left: 8px; top: 32px; }
  .service--bath { left: 198px; top: 32px; }
  .service--reno { left: 31px; top: 55px; }
  .service--ext { left: 237px; top: 55px; }

  /* contact side */
  .brand { position: absolute; left: 0; right: 0; top: 88px; text-align: center;
    font-family: "Questrial", sans-serif; color: var(--brand-blue); }
  .brand__name { display: inline-flex; align-items: center; gap: 6px; font-size: 16px; line-height: 1; }
  .brand__mark { width: 10px; height: 10px; background: var(--brand-blue); }
  .brand__sub { display: flex; align-items: center; justify-content: center; gap: 4px;
    margin-top: 2px; font-size: 11px; color: var(--ink-grey); }
  .brand__sub::before, .brand__sub::after { content: ""; width: 24px; height: 1px; background: var(--brand-blue); }
  .brand__and { font-size: 5px; letter-spacing: 4.6px; color: var(--ink-grey); margin-top: 1px; }
  .brand__tagline { display: inline-block; font-family: "Roboto Slab", serif; font-weight: 300;
    font-size: 10px; color: var(--brand-blue); border-bottom: 1px solid var(--brand-blue); padding: 0 2px 1px; }

  .contact { position: absolute; left: 45px; top: 180px; width: 386px; height: 56px;
    border-top: 1px solid var(--rule-blue); border-bottom: 1px solid var(--rule-blue); }
  .contact__divider { position: absolute; left: 156px; top: 0; bottom: 0; width: 1px; background: var(--rule-blue); }
  .person { position: absolute; right: 239px; top: 13px; text-align: right; font-family: "Questrial", sans-serif; }
  .person__name { font-size: 16px; color: var(--brand-blue); letter-spacing: -0.2px; line-height: 1; }
  .person__role { font-size: 9px; color: #333; margin-top: 2px; }
  .details { position: absolute; left: 167px; top: 4px; list-style: none;
    font-family: "Questrial", sans-serif; font-size: 11.5px; color: #3a3d42; }
  .details li { display: flex; align-items: center; gap: 6px; height: 16.5px; }
  .details svg { width: 10px; height: 10px; flex: none; }
</style>
</head>
<body>
<main class="canvas">

  <section class="card card--services">
    <div class="card__photo" role="img" aria-label="Blue-toned photo of a builder in a hard hat and vest reviewing plans at a house frame construction site"></div>
    <ul class="services">
      <li class="service service--newbuilds"><svg viewBox="0 0 10 10"><path d="M1 5.5 L4 8.5 L9 1.5" fill="none" stroke="#fff" stroke-width="1.2"/></svg>New builds and granny flats</li>
      <li class="service service--home"><svg viewBox="0 0 10 10"><path d="M1 5.5 L4 8.5 L9 1.5" fill="none" stroke="#fff" stroke-width="1.2"/></svg>Home improvement projects</li>
      <li class="service service--bath"><svg viewBox="0 0 10 10"><path d="M1 5.5 L4 8.5 L9 1.5" fill="none" stroke="#fff" stroke-width="1.2"/></svg>Bathroom and kitchen renovations</li>
      <li class="service service--reno"><svg viewBox="0 0 10 10"><path d="M1 5.5 L4 8.5 L9 1.5" fill="none" stroke="#fff" stroke-width="1.2"/></svg>House renovations</li>
      <li class="service service--ext"><svg viewBox="0 0 10 10"><path d="M1 5.5 L4 8.5 L9 1.5" fill="none" stroke="#fff" stroke-width="1.2"/></svg>House extensions</li>
    </ul>
  </section>

  <section class="card card--contact">
    <div class="card__photo" role="img" aria-label="Faded photo of builders in hard hats in front of a scaffolded two-storey house under construction"></div>
    <div class="brand">
      <div class="brand__name"><span class="brand__mark"></span>Riverstone &amp; Pine</div>
      <div class="brand__sub">Construction</div>
      <div class="brand__and">AND DEVELOPMENTS</div>
      <div class="brand__tagline">Built on solid ground!</div>
    </div>
    <div class="contact">
      <div class="person">
        <div class="person__name">Omar Haddine</div>
        <div class="person__role">Director</div>
      </div>
      <div class="contact__divider"></div>
      <ul class="details">
        <li><svg viewBox="0 0 10 10"><circle cx="5" cy="5" r="5" fill="var(--brand-blue)"/><path d="M3.2 2.6 L4.2 2.4 L4.6 3.8 L4 4.3 Q4.6 5.6 5.7 6 L6.2 5.4 L7.6 5.8 L7.4 6.8 Q4 7.2 3.2 2.6Z" fill="#fff"/></svg>555-010-247</li>
        <li><svg viewBox="0 0 10 10"><circle cx="5" cy="5" r="5" fill="var(--brand-blue)"/><rect x="2.5" y="3.2" width="5" height="3.6" fill="#fff"/><path d="M2.5 3.2 L5 5.2 L7.5 3.2" fill="none" stroke="var(--brand-blue)" stroke-width="0.6"/></svg>omar@rpcbuildgroup.com.au</li>
        <li><svg viewBox="0 0 10 10"><circle cx="5" cy="5" r="5" fill="var(--brand-blue)"/></svg>rpc_buildgroup</li>
      </ul>
    </div>
  </section>

</main>
</body>
</html>
```